Update our business cards to match our awesome new website

Need a new design for company business cards. We have recently revamped our website and would like our business cards to get a refresh too. I've uploaded the company artwork, logo, as well as the Branding Deck to better understand the look & feel of our brand. Please visit the website at hollowbrookestatesmi.com.

Industry/Entity Type

Real Estate

Contact Information for Business Card

must use the colors outlined in the Branding Deck uploaded to the site, or the colors of our logo.

Font styles to use
Other font styles liked:
• Calibri

Requirements
Must have
• Required items: Name, title, company logo, address: 218 Fenwick St. Suite 300, Northville, MI 48173, email address: cole@hollowbrookestatesMI.com, company phone 800-555-0193, cell: 248-555-0162
Nice to have
• a more simple design. not complicated
Should not have
• cartoonish characters, or whimsical writing or artwork, stay within our branding colors

```html
<!DOCTYPE html>
<html lang="en">
<head>
<meta charset="utf-8">
<title>Hollowbrook Estates – Business Cards</title>
<link rel="stylesheet" href="https://fonts.googleapis.com/css2?family=Open+Sans:wght@400;600;700&display=swap">
<style>
  :root {
    --brand-green: #0e6049;
    --brand-blue: #2a8fcf;
    --card-white: #f4f4f4;
    --ink: #2b2b2b;
    --rule: #9a9a9a;
    --backdrop: #e4e4e4;
  }
  * { box-sizing: border-box; margin: 0; padding: 0; }
  html, body { width: 1200px; height: 960px; overflow: hidden; }
  body {
    background: var(--backdrop);
    font-family: "Open Sans", Calibri, sans-serif;
    color: var(--ink);
    position: relative;
  }
  .card {
    position: absolute;
    left: 303px;
    width: 597px;
    height: 341px;
  }
  .card-front { top: 114px; background: var(--brand-green); }
  .card-back { top: 507px; background: var(--card-white); }

  .brand-name {
    position: absolute;
    left: 0; right: 0;
    text-align: center;
    font-weight: 600;
    letter-spacing: 0.5px;
  }
  .card-front .brand-name {
    top: 148px;
    font-size: 36px;
    color: #ffffff;
  }
  .card-back .brand-name {
    top: 100px;
    font-size: 30px;
    color: var(--brand-green);
  }

  .person {
    position: absolute;
    top: 163px;
    left: 0; right: 0;
    text-align: center;
  }
  .person-name {
    font-size: 20px;
    font-weight: 700;
    color: var(--brand-green);
    letter-spacing: 0.3px;
    line-height: 26px;
  }
  .person-title {
    font-size: 13px;
    line-height: 20px;
  }
  .divider {
    width: 62px;
    height: 1px;
    background: var(--rule);
    margin: 12px auto 0;
  }
  .contact {
    position: absolute;
    top: 231px;
    left: 0; right: 0;
    text-align: center;
    font-size: 14px;
    line-height: 21px;
  }
  .contact-row { display: flex; justify-content: center; align-items: center; gap: 18px; }
  .contact-item { display: inline-flex; align-items: center; gap: 4px; }
  .contact-item svg { width: 13px; height: 13px; }
  .address {
    position: absolute;
    top: 285px;
    left: 0; right: 0;
    text-align: center;
    font-size: 14px;
  }
  .web-band {
    position: absolute;
    left: 0; right: 0; bottom: 0;
    height: 28px;
    background: var(--brand-green);
    color: #ffffff;
    text-align: center;
    font-size: 14px;
    font-weight: 600;
    line-height: 28px;
  }
  .web-band .domain { color: var(--brand-blue); }
</style>
</head>
<body>
  <section class="card card-front">
    <div class="brand-name">Hollowbrook Estates</div>
  </section>

  <section class="card card-back">
    <div class="brand-name">Hollowbrook Estates</div>

    <div class="person">
      <div class="person-name">DANIEL WHITAKER</div>
      <div class="person-title">President</div>
      <div class="divider"></div>
    </div>

    <div class="contact">
      <div class="contact-row">
        <span class="contact-item">
          <svg viewBox="0 0 16 16" aria-hidden="true"><path fill="#2a8fcf" d="M3.6 1.2l2.3 2.6-1.3 1.7c.9 2 2.6 3.7 4.6 4.6l1.7-1.3 2.6 2.3-1.6 2.3C6.5 15 1 9.5 1.3 2.8z"/></svg>
          800-555-0193
        </span>
        <span class="contact-item">
          <svg viewBox="0 0 16 16" aria-hidden="true"><rect x="4" y="1" width="8" height="14" rx="1.5" fill="none" stroke="#2a8fcf" stroke-width="1.5"/><circle cx="8" cy="12.5" r="0.9" fill="#2a8fcf"/></svg>
          248-555-0162
        </span>
      </div>
      <div class="contact-row">
        <span class="contact-item">
          <svg viewBox="0 0 16 16" aria-hidden="true"><rect x="1" y="3" width="14" height="10" fill="none" stroke="#2a8fcf" stroke-width="1.5"/><path d="M1 3l7 6 7-6" fill="none" stroke="#2a8fcf" stroke-width="1.5"/></svg>
          cole@hollowbrookestatesMI.com
        </span>
      </div>
    </div>

    <div class="address">218 Fenwick St. Suite 300, Northville, MI 48173</div>

    <div class="web-band">www.<span class="domain">hollowbrookestatesMI</span>.com</div>
  </section>
</body>
</html>
```